postcard design for a design company to promote itself in a new area

I am putting out postcards to hairdressing salons that I have renovated recently to target there client base and to offer a discount to the initial consult to there loyal clients. I would like to have a vibrant front design that I can change every twelve weeks with my logo (existing) imbedding into a vibrate, energetic, stylish yet creative front. I want something very colourful fun and inviting that makes people want to pick it up, it should contain some style of pattern and I don't want it all to be my logo. My existing logo I would like on the front but only small or built into the pattern it can be in a different colour and the out side shape can change as long its still the same letters etc.. The pattern can contain words.. The following is what I have written that will be on the back of the post card so you can understand the feel of it.

Marlie from Kestrel Interiors is partnering up with Bellora and Gwenda from Pim Locks
As we have something special in common, we both want our clients to look & feel fabulous
Marlie is offering the loyal clients of Pim Locks a special in home consult at a reduced rate.
What we do: Create innovative yet practical design solutions, window treatments & furniture, which are stylish, happy & memorable. Design to us is about you, who you are & how you live, we are passionate about creating a space that is for you and about you.
A well-designed space makes you feel 10 years younger and truly fabulous to be in, it does not have to cost the earth, but it is something everyone should go home to…
Call today to find out how we can add value & create a space that makes you feel wonderful to be in.
m 0413 925 716

Any suggestions on the wording would be appreciated... Especially the 'A well designed space makes you feel 10years younger'

I have attached my existing logo the colour can change.

I want to reach out to the people sitting in the chair getting there hair done and make them want to know a little more about my business. I would like the post card to feel fresh young new and happy.

```html
<!DOCTYPE html>
<html lang="en">
<head>
<meta charset="utf-8">
<title>Kestrel Interiors – Postcard</title>
<link rel="stylesheet" href="https://fonts.googleapis.com/css2?family=Didact+Gothic&family=Questrial&family=Kalam:wght@400&display=swap">
<style>
  :root {
    --charcoal: #2c2c2e;
    --charcoal-edge: #3a3a3d;
    --magenta: #e62aa4;
    --cyan: #1ed3e6;
    --lime: #7fc41f;
    --white: #ffffff;
    --ink: #2a2a2a;
    --paper: #ffffff;
  }
  * { box-sizing: border-box; margin: 0; padding: 0; }
  html, body { width: 1200px; height: 1150px; overflow: hidden; background: var(--paper); }
  .canvas { position: relative; width: 1200px; height: 1150px; }

  .postcard {
    position: absolute; left: 70px; width: 1060px; overflow: hidden;
    background: var(--charcoal);
    box-shadow: 0 2px 6px rgba(0,0,0,.35);
  }
  .postcard--front { top: 63px; height: 502px; }
  .postcard--back  { top: 584px; height: 498px; }
  .waves { position: absolute; inset: 0; width: 100%; height: 100%; }

  .photo {
    position: absolute;
    box-shadow: 6px 8px 14px rgba(0,0,0,.55);
  }
  .photo--dining  { left: 44px;  top: 67px;  width: 235px; height: 288px;
    background: linear-gradient(135deg, #b7c92a 0%, #8c9a3a 45%, #b89a6c 80%, #e9e2d4 100%); }
  .photo--bedroom { left: 297px; top: 127px; width: 274px; height: 184px;
    background: linear-gradient(160deg, #f3f1ec 0%, #cfdde6 30%, #e6a77a 65%, #d88a5e 100%); }
  .photo--dresser { left: 590px; top: 70px;  width: 241px; height: 270px;
    background: linear-gradient(180deg, #f4f2ee 0%, #3f8fc4 30%, #d9d6cf 50%, #6b1f24 70%, #4a1418 100%); }

  .brand-tile {
    position: absolute; width: 170px; height: 172px;
    background: var(--charcoal);
    border: 1px solid var(--charcoal-edge);
    box-shadow: 5px 7px 14px rgba(0,0,0,.5);
    display: flex; flex-direction: column; align-items: center; justify-content: center;
    color: var(--white);
    font-family: "Didact Gothic", sans-serif;
    font-size: 19px; letter-spacing: 2px; line-height: 1.35; text-align: center;
  }
  .postcard--front .brand-tile { left: 857px; top: 292px; }
  .postcard--back  .brand-tile { left: 844px; top: 282px; width: 178px; height: 181px; }

  .tagline {
    position: absolute; left: 44px; top: 432px;
    font-family: "Kalam", cursive;
    font-size: 25px; color: var(--white);
  }

  .message {
    position: absolute; left: 66px; top: 57px; width: 921px; height: 375px;
    background: var(--white);
    box-shadow: 5px 7px 14px rgba(0,0,0,.45);
    padding: 18px 50px 0 30px;
    font-family: "Didact Gothic", sans-serif;
    color: var(--ink); font-size: 16.5px; line-height: 1.3;
  }
  .message__intro { text-align: center; padding: 0 20px; }
  .message__heading {
    font-family: "Questrial", sans-serif; font-weight: 700;
    color: var(--cyan); font-size: 23px; text-align: center;
    margin: 14px 0 10px; letter-spacing: .5px;
  }
  .message__services { text-align: center; padding: 0 20px; }
  .message__promise { margin-top: 12px; }
  .message__call {
    font-family: "Kalam", cursive; font-size: 15px; margin-top: 14px;
  }
  .message__phone {
    font-family: "Questrial", sans-serif; font-weight: 700;
    color: var(--cyan); font-size: 23px; margin-top: 16px;
  }
</style>
</head>
<body>
<div class="canvas">

  <section class="postcard postcard--front">
    <svg class="waves" viewBox="0 0 1060 502" preserveAspectRatio="none" aria-hidden="true">
      <path fill="var(--white)" d="M0,90 C200,60 400,120 600,250 C750,340 900,380 1060,330 V400 C900,440 700,420 560,350 C380,260 200,180 0,200Z"/>
      <path fill="var(--lime)" d="M0,60 C250,30 450,120 620,230 C760,320 920,330 1060,280 V330 C900,380 760,370 620,290 C450,180 250,100 0,115Z"/>
      <path fill="var(--cyan)" d="M0,20 C250,0 480,90 640,200 C780,290 920,270 1060,220 V285 C920,330 770,320 630,230 C470,120 250,50 0,75Z"/>
      <path fill="var(--magenta)" d="M140,0 H700 C820,40 950,120 1060,150 V215 C920,260 780,240 650,160 C520,80 350,20 140,0Z"/>
      <path fill="none" stroke="#111" stroke-width="6" d="M0,78 C250,52 470,120 630,232 C770,322 920,332 1060,286"/>
    </svg>

    <div class="photo photo--dining" role="img" aria-label="Photo of a lime-green dining setting with white lilies and glassware"></div>
    <div class="photo photo--bedroom" role="img" aria-label="Photo of a sunny bedroom with a peach floral bedspread by the window"></div>
    <div class="photo photo--dresser" role="img" aria-label="Photo of a dark red dresser with plants in glass vases below blue artwork"></div>

    <div class="brand-tile"><span>KESTREL</span><span>INTERIORS</span></div>

    <p class="tagline">We can add value &amp; create a space that makes you feel wonderful to be in.</p>
  </section>

  <section class="postcard postcard--back">
    <svg class="waves" viewBox="0 0 1060 498" preserveAspectRatio="none" aria-hidden="true">
      <path fill="var(--cyan)" d="M0,0 H340 C300,90 200,170 0,210Z"/>
      <path fill="var(--cyan)" d="M1060,50 C900,70 700,130 580,200 L590,235 C720,170 900,115 1060,115Z"/>
      <path fill="var(--lime)" d="M0,320 C160,330 360,310 520,230 C700,140 880,90 1060,110 V135 C880,118 700,168 530,255 C370,335 170,352 0,348Z"/>
      <path fill="var(--magenta)" d="M260,0 H1060 V110 C880,90 700,140 520,230 C360,310 160,330 0,320 V240 C180,240 260,100 260,0Z"/>
    </svg>

    <div class="message">
      <p class="message__intro">Marlie from Kestrel Interiors is partnering up with Bellora and Gwenda from Pim Locks As we have something special in common, we both want our clients to look &amp; feel fabulous Marlie is offering the loyal clients of Pim Locks a special in home consult at a reduced rate.</p>
      <h2 class="message__heading">WHAT WE DO</h2>
      <p class="message__services">Create innovative yet practical design solutions, window treatments &amp; furniture, which are stylish, happy &amp; memorable. Design to us is about you, who you are &amp; how you live, we are passionate about creating a space that is for you and about you.</p>
      <p class="message__promise">A well-designed space makes you feel 10 years younger and truly fabulous to be in,<br>it does not have to cost the earth, but it is something everyone should go home to…</p>
      <p class="message__call">Call today to find out how we can add value &amp; create a space that makes you feel wonderful to be in.</p>
      <p class="message__phone">M 0413 925 716</p>
    </div>

    <div class="brand-tile"><span>KESTREL</span><span>INTERIORS</span></div>
  </section>

</div>
</body>
</html>
```